Corporate Web Redesign Project - coded

We would like redesign/refresh of our current site that would allow us to increase the depth of content and create a high quality impression for visitors.

Current site - http://corvanisystems.com/

A previous web redesign project has improved our site but it has not really reached the level we require.

Our customers are global, blue chip, organisations and a professional, corporate style of site is required.

Please note we would prefer a coded website to a just a design. We are happy to provide a zip of our current site if required.
Updates

                                   

Target Market(s)

Global oil and gas producers, KR, Tamberline, Orvadex etc.

Industry/Entity Type

It Professional

Requirements
Must have
• Design should support the level of content we currently have in the existing sitemap - although it should be expandable a site design for a large / complex site would not be appropriate

All current content / pages to be reflected in design

Must be visually appealing

Intuitive and clear navigation that is expandable

Display a high level of professionalism

Use a consistent palette of colours that complements our logo

Clean and organized layout

A way to capture visitor’s information or Call to action (i.e. contact link or form) on every page

Prominent Contact Information
Should not have
• Flash

```html
<!DOCTYPE html>
<html lang="en">
<head>
<meta charset="utf-8">
<title>LRX - Lessons Learned Software | Corvani Systems</title>
<link rel="stylesheet" href="https://fonts.googleapis.com/css2?family=Bebas+Neue&family=Open+Sans:ital,wght@0,400;0,600;0,700;1,400&display=swap">
<style>
:root{
  --teal:#2e6670;
  --teal-light:#4b838b;
  --teal-dark:#24535b;
  --ink:#3a3431;
  --text:#3d3d3d;
  --orange:#e5782a;
  --band:#eceeeb;
  --panel:#e7ecee;
  --strip:#eceff0;
  --white:#ffffff;
  --footer-muted:#5f8e96;
  --footer-text:#9fbfc4;
}
*{box-sizing:border-box;margin:0;padding:0}
html,body{width:863px;height:1200px;overflow:hidden;background:var(--white)}
body{position:relative;font-family:"Open Sans",Arial,sans-serif;color:var(--text)}
.display{font-family:"Bebas Neue",Impact,sans-serif;font-weight:400;color:var(--ink)}
a{color:var(--orange)}
.abs{position:absolute}

/* header */
.brand{left:94px;top:24px;display:flex;align-items:center;gap:10px}
.brand-dot{width:46px;height:46px;border-radius:50%;background:var(--teal)}
.brand-name{font-family:"Open Sans",Arial,sans-serif;font-weight:700;font-size:22px;color:var(--teal);letter-spacing:1px}
.office{top:16px;font-size:9.6px;line-height:11.6px;color:var(--teal)}
.office h4{font-family:"Bebas Neue",Impact,sans-serif;font-weight:400;font-size:17px;line-height:18px;color:var(--teal);margin-bottom:1px}
.office--eu{left:496px}
.office--na{left:652px}

/* nav */
.nav{left:0;top:107px;width:863px;height:30px;background:var(--teal);display:flex;padding-left:95px}
.nav a{color:var(--white);text-decoration:none;font-size:12.5px;text-transform:uppercase;line-height:30px;padding:0 12px}
.nav a.is-active{background:var(--teal-light)}

/* title band */
.title-band{left:0;top:137px;width:863px;height:99px;background:var(--band)}
.page-title{left:94px;top:165px;font-size:50px;line-height:50px}

/* content */
.intro{left:94px;top:269px;width:448px;font-size:9.7px;line-height:13.4px}
.intro p{margin-bottom:13.4px}
.section-title{font-size:27px;line-height:28px}
.loc-title{left:94px;top:485px}
.loc{top:525px;font-size:9.7px;line-height:13.2px}
.loc h5{font-family:"Bebas Neue",Impact,sans-serif;font-weight:400;font-size:16px;line-height:17px;color:var(--ink)}
.loc--eu{left:94px}.loc--na{left:324px}
.map{top:624px;width:216px;height:214px;background:linear-gradient(160deg,#efe9dc,#e4ddc9 55%,#d9dccf)}
.map--eu{left:94px}.map--na{left:324px}

/* sidebar */
.panel{left:553px;width:215px;background:var(--panel)}
.news{top:274px;height:325px;padding:10px 16px}
.news .section-title{margin:4px 0 10px}
.news-head{font-size:10px;font-weight:700;color:var(--orange);line-height:13px}
.news p{font-size:9.8px;line-height:13px;font-style:italic;color:var(--text)}
.news .quote{margin-top:12px}
.news .who{font-size:10px;font-weight:700;color:var(--orange);font-style:normal}
.quick{top:618px;height:251px;padding:12px 14px}
.quick .section-title{margin-bottom:9px}
.field{display:block;width:187px;height:24px;background:var(--white);border:1px solid #cfd6d8;font-size:9.5px;padding:6px 7px;margin-bottom:9px;color:#555}
.field--msg{height:60px}
.submit{position:absolute;right:14px;bottom:12px;width:86px;height:28px;background:var(--teal-dark);color:var(--white);font-family:"Bebas Neue",Impact,sans-serif;font-size:17px;text-align:center;line-height:29px}

/* clients */
.clients{left:0;top:900px;width:863px;height:75px;background:var(--strip);display:flex;justify-content:space-between;align-items:center;padding:0 120px 0 122px}
.client{font-weight:600;font-size:12px;color:#6a6f72}

/* footer */
.footer{left:0;top:975px;width:863px;height:225px;background:var(--teal)}
.fcol{top:995px;width:160px}
.fcol h4{font-family:"Bebas Neue",Impact,sans-serif;font-weight:400;font-size:17px;color:var(--white);margin-bottom:28px}
.f1{left:94px}.f2{left:266px}.f3{left:439px}.f4{left:612px}
.fcol p{font-size:9.4px;line-height:11.8px;color:var(--footer-muted)}
.byline{text-align:right;font-style:italic;margin-top:8px}
.partner-badge{width:155px;height:28px;border-radius:3px;background:var(--footer-muted)}
.social{display:flex;gap:9px}
.social span{width:28px;height:28px;border-radius:50%;background:var(--footer-muted)}
.fcol p.contact{color:var(--footer-text);margin-bottom:12px}
.fcol p.contact a{color:var(--white)}
.copyright{left:0;top:1176px;width:863px;text-align:center;font-size:10px;color:var(--white);font-weight:600}
</style>
</head>
<body>

<header>
  <div class="abs brand"><span class="brand-dot"></span><span class="brand-name">CORVANI SYSTEMS</span></div>
  <div class="abs office office--eu">
    <h4>Europe</h4>
    18 Kelburn Row<br>Aberdeen<br>AB12 4QT<br>Phone:+44(0)1224 555014<br>Email: <a href="#">eu@corvanisystems.com</a>
  </div>
  <div class="abs office office--na">
    <h4>North America</h4>
    4100 Westmere Pkwy<br>Suite 300<br>Houston, TX 77042<br>Phone:(713) 555 0148<br>Email: <a href="#">us@corvanisystems.com</a>
  </div>
</header>

<nav class="abs nav">
  <a href="#">Home</a><a href="#">News</a><a href="#">About Us</a><a href="#" class="is-active">Solutions</a><a href="#">Contact Us</a>
</nav>

<div class="abs title-band"></div>
<h1 class="abs display page-title">LRX - Lessons Learned Software</h1>

<main>
  <div class="abs intro">
    <p>LRX emulates your current processes for tracking operational lessons learned and event details. It has a flexible structure to allow the mapping of your workflows and provides a fully searchable repository of lessons and downtime information.<br>By mapping your own workflows, LRX has unprecedented levels of adoption across organizations. It achieves its goal of being a simple to use and effective tool whilst also being fully featured with flexible and customizable reporting.</p>
    <p>While featuring a full search facility for browsing lessons, the LRX system also categorizes lessons learned to allow easy reporting in advance of any phase or operation. By cutting effort at every step, LRX allows staff to concentrate on core operations rather than searching through paper.</p>
    <p>The system is built using Stratum with integrated Keyring Directory authentication and Single Sign On, so it is both easy to use and easy to implement across your organization.</p>
    <p>For more information about LRX please email: <a href="#">LRXEnquiries@corvanisystems.com</a></p>
  </div>

  <h2 class="abs display section-title loc-title">Locations</h2>
  <div class="abs loc loc--eu">
    <h5>Europe</h5>
    18 Kelburn Row<br>Aberdeen<br>AB12 4QT<br>Phone:+44(0)1224 555014<br>Email: <a href="#">eu@corvanisystems.com</a>
  </div>
  <div class="abs loc loc--na">
    <h5>North America</h5>
    4100 Westmere Pkwy<br>Suite 300<br>Houston, TX 77042<br>Phone:(713) 555 0148<br>Email: <a href="#">us@corvanisystems.com</a>
  </div>
  <div class="abs map map--eu" role="img" aria-label="Street map of the Aberdeen office location"></div>
  <div class="abs map map--na" role="img" aria-label="Street map of the Houston office location"></div>
</main>

<aside>
  <section class="abs panel news">
    <h2 class="display section-title">LRX News</h2>
    <div class="news-head">KR upgrade to LRX (Crewlink) 4.0</div>
    <p>KR operates LRX under the name Crewlink across its Global Wells Organisation and into parts of its downstream business. LRX 4.0 upgrades the sharing and management of learnings for KR in 37 teams across the globe.</p>
    <p class="quote">"Corvani Systems' system has greatly helped me in the active tracking of lessons learned, allowing efficient searches of any field of the database. It is a major improvement on the previous system I used, cutting out a lot of the tedium and exhaustive searching. The CVS engineers were extremely flexible in tailoring the software to cater for our precise needs, producing a system that performs exactly as required."<br><span class="who">Technical Assistant</span></p>
  </section>

  <section class="abs panel quick">
    <h2 class="display section-title">Reach Us Quickly</h2>
    <span class="field">Your Name</span>
    <span class="field">Your Email</span>
    <span class="field field--msg">Message</span>
    <span class="submit">Submit</span>
  </section>
</aside>

<div class="abs clients">
  <span class="client">Orvadex</span>
  <span class="client">Tessaro</span>
  <span class="client">Palisade</span>
  <span class="client">Wendmoor</span>
  <span class="client">KR</span>
  <span class="client">Quenta</span>
  <span class="client">Halvern</span>
</div>

<footer>
  <div class="abs footer"></div>
  <div class="abs fcol f1">
    <h4>Testimonials</h4>
    <p>Lorem ipsum dolor sit amet, consectetur adipisicing elit, sed do eiusmod tempor incididunt ut labore et dolore magna aliqua. Uugiat nulla pariatur. Excepteur sint occaecat cupidatat non proident, sunt in culpa qui officia deserunt mollit anim id est laborum.</p>
    <p class="byline">by Mara Delling</p>
  </div>
  <div class="abs fcol f2">
    <h4>Partner</h4>
    <div class="partner-badge"></div>
    <p style="margin-top:3px">Gold Independent Software Vendor (ISV)</p>
  </div>
  <div class="abs fcol f3">
    <h4>Follow Us</h4>
    <div class="social"><span></span><span></span><span></span><span></span></div>
  </div>
  <div class="abs fcol f4">
    <h4>Get In Touch</h4>
    <p class="contact">18 Kelburn Row<br>Aberdeen<br>AB12 4QT<br>Phone:+44(0)1224 555014<br>Email: <a href="#">eu@corvanisystems.com</a></p>
    <p class="contact">4100 Westmere Pkwy<br>Suite 300<br>Houston, TX 77042<br>Phone:(713) 555 0148<br>Email: <a href="#">us@corvanisystems.com</a></p>
  </div>
  <div class="abs copyright">Copyright © Corvani Systems Ltd 2013</div>
</footer>

</body>
</html>
```